Prepared ready to cook meal delivery service needs a flyer design

We need a flyer design for a startup company based in Cape Town, South Africa. I've attached a few flyer designs that I like.

The company is called 'Brindle' and our website will be found at brindle.co.za. We don't have a logo yet.

Flyer text:

Brindle
Ready to roast

Do you feel like a home cooked meal but don't like shopping, peeling, chopping, cooking, or cleaning up?

We deliver ready to roast free range chicken and fresh vegetables to your door.

To order: SMS your name to 083 614 2958 and we'll call you back.

Only the best ingredients used
Free range chickens. Fresh herbs and vegetables. Virgin olive oil.

No bad carbs!

Ready to roast Free range chicken and fresh veggies
For 2 R99
For 4 R139
Updates

Wording of flyer updated.

Target Market(s)

Local Cape Townians that hate grocery shopping and need help saving time preparing meals.

Industry/Entity Type

Delivery Service

Requirements
Must have
• To find out more: SMS your name to 083 614 2958

```html
<!DOCTYPE html>
<html lang="en">
<head>
<meta charset="utf-8">
<title>Brindle – Ready to Roast</title>
<link rel="stylesheet" href="https://fonts.googleapis.com/css2?family=Fredoka:wght@600&family=Josefin+Sans:wght@600;700&family=Anton&family=Archivo+Narrow:wght@500&family=Oswald:wght@500&display=swap">
<style>
  :root {
    --paper: #ece3d3;
    --paper-dark: #d9cdb8;
    --smoke: #a9a49d;
    --orange: #f26522;
    --orange-soft: #f3a375;
    --red: #e2222b;
    --ink: #1b1b1b;
    --white: #ffffff;
    --flame-red: #e8341c;
    --flame-yellow: #ffc21a;
  }
  * { box-sizing: border-box; margin: 0; padding: 0; }
  html, body { width: 846px; height: 1200px; overflow: hidden; background: var(--paper); }
  .flyer {
    position: relative; width: 846px; height: 1200px; overflow: hidden;
    background:
      radial-gradient(ellipse 520px 170px at 50% 20px, var(--smoke), transparent 75%),
      radial-gradient(ellipse 700px 500px at 50% 60%, var(--paper), var(--paper-dark));
    font-family: "Josefin Sans", sans-serif; color: var(--ink);
  }
  .badge-quality {
    position: absolute; left: 18px; top: 8px; width: 180px; height: 160px;
    background: var(--white); border: 9px solid var(--orange); border-radius: 48% 52% 50% 46%;
    display: flex; align-items: center; justify-content: center; text-align: center;
    font-family: "Anton", sans-serif; font-size: 24px; line-height: 1.0; text-transform: uppercase;
  }
  .emblem {
    position: absolute; left: 184px; top: 25px; width: 480px; height: 480px; border-radius: 50%;
    background: var(--white); border: 4px solid var(--orange);
  }
  .brand-name {
    position: absolute; left: 0; width: 846px; top: 198px; text-align: center;
    font-family: "Fredoka", sans-serif; font-weight: 600; font-size: 104px; letter-spacing: 2px; color: var(--ink);
  }
  .stripe {
    position: absolute; left: 0; top: 392px; width: 846px; height: 40px; background: var(--red);
    border-top: 3px solid var(--white); border-bottom: 3px solid var(--white);
    box-shadow: 0 0 0 2px var(--red);
  }
  .title-box {
    position: absolute; left: 155px; top: 378px; width: 553px; height: 80px; background: var(--orange);
    box-shadow: 3px 4px 6px rgba(0,0,0,.35);
    display: flex; align-items: center; justify-content: center;
    font-family: "Fredoka", sans-serif; font-weight: 600; font-size: 58px; color: var(--white);
  }
  .flames {
    position: absolute; left: 20px; top: 460px; width: 806px; height: 95px;
    background: linear-gradient(to top, var(--flame-red), var(--orange) 45%, var(--flame-yellow) 85%, transparent);
    opacity: .9;
  }
  .rule { position: absolute; left: 30px; width: 792px; height: 3px; background: var(--ink); }
  .question {
    position: absolute; left: 30px; top: 572px; width: 900px;
    font-size: 25px; font-weight: 600; line-height: 1.28; text-transform: uppercase;
    white-space: nowrap; transform: scaleX(0.87); transform-origin: left top;
  }
  .delivery-banner {
    position: absolute; left: 22px; top: 660px; width: 800px; height: 130px; background: var(--white);
    box-shadow: 2px 4px 8px rgba(0,0,0,.45);
    display: flex; flex-direction: column; align-items: center; justify-content: center;
    font-family: "Oswald", sans-serif; font-weight: 500; text-transform: uppercase; line-height: .98; letter-spacing: 1px;
  }
  .delivery-banner .l1 { font-size: 34px; }
  .delivery-banner .l2 { font-size: 27px; }
  .delivery-banner .l3 { font-size: 33px; }
  .delivery-banner .l4 { font-size: 24px; }
  .track { position: absolute; top: 28px; width: 150px; height: 70px;
    background: linear-gradient(90deg, transparent, rgba(60,60,60,.35), transparent); border-radius: 40px; }
  .track.left { left: 30px; } .track.right { right: 30px; }
  .features {
    position: absolute; left: 28px; top: 800px; width: 222px; height: 212px;
    background: linear-gradient(to right, var(--orange-soft), #f7bd95);
    padding: 14px 0 0 8px;
    font-family: "Archivo Narrow", sans-serif; font-weight: 500; font-size: 29px; line-height: 1.0; color: var(--white);
  }
  .features li { list-style: none; margin-bottom: 10px; white-space: nowrap; }
  .features .cap { color: #5a2a10; }
  .features li:last-child { border-bottom: 2px solid var(--white); padding-bottom: 6px; width: 188px; }
  .dish-photo {
    position: absolute; left: 250px; top: 800px; width: 395px; height: 212px;
    background: radial-gradient(ellipse at 45% 55%, #d9a055, #b9782f 45%, #8d5a3a 75%, #e9e6e0);
  }
  .carbs-badge {
    position: absolute; left: 612px; top: 776px; width: 222px; height: 222px; border-radius: 50%;
    background: var(--orange); border: 5px solid var(--white); box-shadow: 0 0 0 3px var(--orange), 2px 4px 8px rgba(0,0,0,.3);
    display: flex; align-items: center; justify-content: center; text-align: center;
    font-family: "Anton", sans-serif; font-size: 44px; line-height: 1.0; color: var(--white); transform: rotate(6deg);
  }
  .tagline-band {
    position: absolute; left: 0; top: 1018px; width: 846px; height: 60px; background: var(--white);
    display: flex; align-items: center; justify-content: center; gap: 12px;
    font-family: "Fredoka", sans-serif; font-weight: 600; font-size: 42px; color: #2a2a2a;
  }
  .tagline-band .small { font-size: 26px; }
  .tagline-band .line { flex: 1; height: 0; border-top: 2px dotted #333; margin: 0 6px; }
  .price {
    position: absolute; top: 1078px; width: 250px; height: 250px; border-radius: 50%;
    background: var(--white); border: 3px solid var(--ink);
    text-align: center; padding-top: 16px;
    font-family: "Fredoka", sans-serif; font-weight: 600; font-size: 34px; color: var(--orange);
  }
  .price.for-two { left: 6px; } .price.for-four { left: 588px; }
  .order-label {
    position: absolute; left: 0; width: 846px; top: 1080px; text-align: center;
    font-family: "Anton", sans-serif; font-size: 52px; color: var(--orange); line-height: 1;
  }
  .sms-bar {
    position: absolute; left: 0; top: 1140px; width: 846px; height: 48px; background: var(--ink);
    display: flex; align-items: center; justify-content: center;
    font-family: "Anton", sans-serif; font-size: 28px; color: var(--orange); letter-spacing: .5px; white-space: nowrap;
  }
</style>
</head>
<body>
<main class="flyer">
  <div class="badge-quality"><span>Only<br>the best<br>ingredients<br>used</span></div>

  <div class="emblem"></div>
  <div class="brand-name">BRINDLE</div>

  <div class="stripe"></div>
  <h1 class="title-box">Ready to Roast</h1>

  <div class="flames" role="img" aria-label="Row of orange and yellow flames"></div>

  <div class="rule" style="top:557px"></div>
  <p class="question">Do you feel like a home made meal but don’t like<br>shopping, peeling, chopping, cooking, or cleaning up?</p>
  <div class="rule" style="top:645px"></div>

  <section class="delivery-banner">
    <div class="track left" role="img" aria-label="Tyre tracks"></div>
    <div class="track right" role="img" aria-label="Tyre tracks"></div>
    <span class="l1">We deliver ready</span>
    <span class="l2">to roast free range</span>
    <span class="l3">chicken and fresh</span>
    <span class="l4">vegetables to your door</span>
  </section>

  <ul class="features">
    <li><span class="cap">F</span>ree range<br>chickens</li>
    <li><span class="cap">F</span>resh herbs<br>and vegetables</li>
    <li><span class="cap">V</span>irgin olive oil</li>
  </ul>
  <div class="dish-photo" role="img" aria-label="Photo of a whole roast chicken with vegetables in a white dish"></div>

  <div class="carbs-badge"><span>NO<br>BAD<br>CARBS!</span></div>

  <div class="tagline-band">
    <span class="line"></span>
    <span>Ready <span class="small">To</span> Roast</span>
    <span class="line"></span>
  </div>

  <div class="price for-two">For 2 R99</div>
  <div class="price for-four">For 4 R139</div>
  <div class="order-label">TO ORDER</div>

  <div class="sms-bar">SMS YOUR NAME TO 083 614 2958 AND WE’LL CALL YOU BACK</div>
</main>
</body>
</html>
```